Wrap for Porchlight Pals porchlightpals.com

We’re looking for a creative, detail-oriented designer to create a bold, western-themed vehicle wrap for our company, Porchlight Pals (porchlightpals.com | 800-555-0143). The wrap should help our fleet stand out and instantly communicate our fun, professional, “Texas cowboy” brand identity—think red, white, and blue, cowboy hats, stars, boots, and that classic ranch feel!
About Us:
Porchlight Pals is a fast-growing home services company based in Florida, known for reliable repairs, a can-do attitude, and our cowboy-inspired branding. Our mascot and our logo (see attached images) feature a friendly cowboy in overalls, gloves, and a big hat, with colors and style that pop.
What We Need:
A full vehicle wrap design for a work van or truck
Design must incorporate our branding elements:
Our cowboy mascot (see reference images attached)
Our logo (see attached PNG)
Our brand colors: Red, blue, white
Our website (porchlightpals.com) and phone number (800-555-0143) clearly visible
Western/ranch theme throughout: hats, stars, rope details, badge shapes, etc.
Fun, professional, and memorable—NOT cheesy or clip-art
Side, rear, and hood designs (templates provided after award if needed)
Scalable and print-ready file (vector preferred)
References:
[Attach the mascot image, logo PNG, and any sample vehicle pics if you have them]
Ideal Designer:
Experience designing vehicle wraps (with portfolio examples)
Skilled at cartoon/mascot illustration and western/retro themes
Able to provide all files needed for print and installation
Deliverables:
Full wrap design (all sides) as scalable vector (AI, EPS, PDF)
Mockup of the design on 2014 Brisco Transit Cargo Van
I have the design templete from Tilo Film files.quarvenshare.net/share/folders/8KpqZ2mTr41LbnVy6HeQw0DfAs3CuJgPk?src=share_link
Print-ready files for wrap company
Home Owners

```html
<!DOCTYPE html>
<html lang="en">
<head>
<meta charset="utf-8">
<title>Porchlight Pals — Van Wrap Presentation</title>
<link href="https://fonts.googleapis.com/css2?family=Barlow+Condensed:wght@600&family=Open+Sans:wght@400&display=swap" rel="stylesheet">
<style>
  :root {
    --wrap-red: #d01f2b;
    --wrap-red-dark: #a8161f;
    --wrap-blue: #2b358f;
    --rope-tan: #c9a46c;
    --rope-shade: #8f6a3a;
    --ink-white: #ffffff;
    --canvas: #ffffff;
    --trim-black: #141414;
    --trim-grey: #3a3a3a;
    --glass: #4a4a4a;
    --glass-light: #d9d9d9;
    --rim-silver: #c8c8c8;
    --lamp-amber: #e9a23b;
    --lamp-white: #f1f1f1;
    --shadow-grey: #5a5a5a;
    --mascot-hat: #8a5a34;
    --mascot-denim: #3b5e9a;
  }
  html, body {
    margin: 0;
    padding: 0;
    width: 1200px;
    height: 1200px;
    overflow: hidden;
    background: var(--canvas);
  }
  .sheet { display: block; width: 1200px; height: 1200px; }
  .band-red { fill: var(--wrap-red); }
  .band-blue { fill: var(--wrap-blue); }
  .trim { fill: var(--trim-black); }
  .trim-soft { fill: var(--trim-grey); }
  .glass { fill: var(--glass); }
  .rim { fill: var(--rim-silver); }
  .lamp-amber { fill: var(--lamp-amber); }
  .lamp-white { fill: var(--lamp-white); }
  .lamp-red { fill: var(--wrap-red-dark); }
  .ground-shadow { fill: url(#ground-fade); }
  .seam { fill: none; stroke: var(--wrap-red-dark); stroke-width: 2; }
  .rope {
    fill: none;
    stroke: var(--rope-tan);
    stroke-width: 14;
  }
  .rope-twist {
    fill: none;
    stroke: var(--rope-shade);
    stroke-width: 14;
    stroke-dasharray: 5 7;
    opacity: 0.55;
  }
  .contact-phone {
    font-family: "Barlow Condensed", "Arial Narrow", sans-serif;
    font-weight: 600;
    fill: var(--ink-white);
  }
  .contact-web {
    font-family: "Open Sans", Arial, sans-serif;
    font-weight: 400;
    fill: var(--ink-white);
  }
  .brand-name {
    font-family: "Barlow Condensed", "Arial Narrow", sans-serif;
    font-weight: 600;
    fill: var(--ink-white);
  }
</style>
</head>
<body>
<svg class="sheet" viewBox="0 0 1920 1920" xmlns="http://www.w3.org/2000/svg">
  <defs>
    <linearGradient id="mascot-tones" x1="0" y1="0" x2="0" y2="1">
      <stop offset="0" stop-color="var(--mascot-hat)"/>
      <stop offset="0.45" stop-color="#c23a3f"/>
      <stop offset="1" stop-color="var(--mascot-denim)"/>
    </linearGradient>
    <linearGradient id="ground-fade" x1="0" y1="0" x2="0" y2="1">
      <stop offset="0" stop-color="var(--shadow-grey)"/>
      <stop offset="1" stop-color="#ffffff" stop-opacity="0"/>
    </linearGradient>
    <linearGradient id="window-sheen" x1="0" y1="0" x2="1" y2="1">
      <stop offset="0" stop-color="var(--glass-light)"/>
      <stop offset="1" stop-color="#8d8d8d"/>
    </linearGradient>
    <clipPath id="side-body">
      <path d="M200 335 C230 290 330 272 452 262 L618 88 C720 74 1100 60 1610 52 Q1655 54 1675 120 L1708 300 L1710 470 L1690 545 L290 545 L270 505 L200 440 Z"/>
    </clipPath>
    <clipPath id="panel-frame-inner">
      <rect x="575" y="40" width="663" height="250" rx="22"/>
    </clipPath>
  </defs>

  <!-- Side view -->
  <g class="van-side">
    <path class="ground-shadow" d="M20 645 L260 585 L1700 585 L1910 645 Z"/>
    <g clip-path="url(#side-body)">
      <rect class="band-red" x="190" y="40" width="1540" height="520"/>
      <path class="band-blue" d="M190 300 L440 262 L615 85 L850 68 C790 80 770 110 770 150 L770 270 L190 275 Z"/>
      <rect class="band-blue" x="190" y="442" width="1460" height="110"/>
      <path class="band-red" d="M1650 430 L1730 430 L1730 560 L1610 560 C1630 520 1645 480 1650 430 Z"/>
    </g>
    <path class="glass" d="M455 262 L600 125 C620 112 735 108 742 118 L745 255 Z"/>
    <path d="M490 240 L605 135 L735 125 L738 240 Z" fill="url(#window-sheen)"/>
    <path class="seam" d="M488 262 L488 500 Q490 520 510 520 L765 518 L770 90"/>
    <rect class="trim" x="728" y="268" width="18" height="52" rx="3"/>
    <rect class="trim" x="190" y="330" width="50" height="102" rx="20"/>
    <rect class="lamp-amber" x="193" y="412" width="46" height="22" rx="6"/>
    <rect class="trim" x="178" y="435" width="125" height="70" rx="14"/>
    <rect class="lamp-red" x="1655" y="135" width="40" height="95" rx="8"/>
    <rect class="trim" x="1685" y="468" width="62" height="66" rx="10"/>

    <rect class="rope" x="862" y="100" width="738" height="305" rx="24"/>
    <rect class="rope-twist" x="862" y="100" width="738" height="305" rx="24"/>
    <path class="band-blue" d="M878 116 H1584 V200 H878 Z"/>

    <rect class="mascot" x="895" y="122" width="235" height="398" rx="26"
          fill="url(#mascot-tones)" role="img"
          aria-label="Cartoon cowboy mascot in hat, plaid shirt, denim overalls, gloves and boots, hands on hips"/>
    <text class="brand-name" x="1330" y="285" font-size="64" text-anchor="middle">PORCHLIGHT PALS</text>

    <text class="contact-phone" x="647" y="372" font-size="42" text-anchor="middle">800-555-0143</text>
    <text class="contact-web" x="647" y="400" font-size="25" text-anchor="middle">porchlightpals.com</text>

    <circle class="trim" cx="400" cy="532" r="106"/>
    <circle class="rim" cx="400" cy="532" r="60"/>
    <circle class="trim-soft" cx="400" cy="532" r="20"/>
    <circle class="trim" cx="1405" cy="535" r="106"/>
    <circle class="rim" cx="1405" cy="535" r="60"/>
    <circle class="trim-soft" cx="1405" cy="535" r="20"/>
  </g>

  <!-- Front view -->
  <g class="van-front">
    <path class="ground-shadow" d="M220 1318 L290 1285 L800 1285 L870 1318 Z"/>
    <rect class="trim" x="237" y="825" width="52" height="65" rx="10"/>
    <rect class="trim" x="797" y="825" width="52" height="65" rx="10"/>
    <path class="band-blue" d="M262 1060 L275 900 L305 790 L775 790 L805 900 L818 1060 Z"/>
    <path class="band-red" d="M330 745 Q345 718 540 716 Q735 718 752 745 L780 830 L300 830 Z"/>
    <path class="band-red" d="M300 905 Q420 880 540 880 Q660 880 780 905 L700 1015 L380 1015 Z"/>
    <rect class="trim" x="305" y="755" width="472" height="152" rx="36"/>
    <rect class="glass" x="340" y="775" width="140" height="100" rx="28"/>
    <rect class="glass" x="608" y="775" width="140" height="100" rx="28"/>
    <rect class="trim-soft" x="478" y="775" width="130" height="95"/>
    <rect class="trim" x="502" y="785" width="80" height="30" rx="6"/>
    <rect class="trim" x="522" y="800" width="40" height="75"/>
    <path class="rope" d="M402 910 Q375 965 402 1012"/>
    <path class="rope" d="M670 910 Q697 965 670 1012"/>
    <text class="brand-name" x="536" y="978" font-size="30" text-anchor="middle">PORCHLIGHT PALS</text>
    <rect class="trim" x="272" y="1010" width="536" height="130" rx="20"/>
    <rect class="trim-soft" x="395" y="1032" width="290" height="100" rx="14"/>
    <rect class="lamp-white" x="298" y="1028" width="58" height="40" rx="8"/>
    <rect class="lamp-white" x="724" y="1028" width="58" height="40" rx="8"/>
    <rect class="lamp-amber" x="270" y="1078" width="112" height="26" rx="4"/>
    <rect class="lamp-amber" x="698" y="1078" width="112" height="26" rx="4"/>
    <rect class="trim" x="258" y="1115" width="562" height="80" rx="22"/>
    <rect class="trim" x="268" y="1185" width="540" height="50" rx="6"/>
    <rect class="trim" x="272" y="1230" width="75" height="72" rx="12"/>
    <rect class="trim" x="730" y="1230" width="75" height="72" rx="12"/>
  </g>

  <!-- Rear view -->
  <g class="van-rear">
    <path class="ground-shadow" d="M1000 1345 L1070 1305 L1645 1305 L1715 1345 Z"/>
    <rect class="trim-soft" x="1018" y="820" width="52" height="70" rx="10"/>
    <rect class="trim-soft" x="1636" y="820" width="52" height="70" rx="10"/>
    <path class="trim" d="M1070 820 Q1095 710 1150 700 Q1350 682 1555 700 Q1610 710 1638 820 Z"/>
    <path class="band-red" d="M1078 820 Q1100 720 1150 712 Q1350 696 1555 712 Q1605 720 1630 820 L1652 1145 L1058 1145 Z"/>
    <rect class="lamp-red" x="1072" y="808" width="38" height="95" rx="8"/>
    <rect class="lamp-red" x="1598" y="808" width="38" height="95" rx="8"/>
    <rect class="band-blue" x="1152" y="752" width="400" height="356" rx="20"/>
    <rect class="rope" x="1145" y="745" width="414" height="370" rx="26"/>
    <rect class="rope-twist" x="1145" y="745" width="414" height="370" rx="26"/>
    <line class="seam" x1="1350" y1="705" x2="1350" y2="1140"/>
    <rect class="trim" x="1368" y="955" width="16" height="50" rx="3"/>
    <text class="brand-name" x="1355" y="875" font-size="44" text-anchor="middle">PORCHLIGHT PALS</text>
    <rect class="mascot" x="1155" y="925" width="100" height="210" rx="16"
          fill="url(#mascot-tones)" role="img"
          aria-label="Small cartoon cowboy mascot in hat and denim overalls, hands on hips"/>
    <text class="contact-phone" x="1395" y="1052" font-size="36" text-anchor="middle">800-555-0143</text>
    <text class="contact-web" x="1395" y="1078" font-size="22" text-anchor="middle">porchlightpals.com</text>
    <rect class="trim" x="1055" y="1145" width="600" height="65" rx="14"/>
    <rect class="trim" x="1150" y="1205" width="410" height="45" rx="20"/>
    <rect class="trim" x="1070" y="1210" width="78" height="120" rx="12"/>
    <rect class="trim" x="1565" y="1210" width="78" height="120" rx="12"/>
  </g>

  <!-- Flat side panel -->
  <g class="wrap-panel" transform="translate(248 1415)">
    <rect class="band-red" x="0" y="0" width="1353" height="465"/>
    <path class="band-blue" d="M0 0 H700 C560 0 458 30 458 120 V205 H0 Z"/>
    <path class="band-blue" d="M0 365 H1275 C1266 405 1252 438 1232 465 H0 Z"/>
    <g clip-path="url(#panel-frame-inner)">
      <rect class="band-blue" x="575" y="40" width="663" height="92"/>
    </g>
    <rect class="rope" x="575" y="40" width="663" height="250" rx="22"/>
    <rect class="rope-twist" x="575" y="40" width="663" height="250" rx="22"/>
    <rect class="mascot" x="610" y="70" width="207" height="390" rx="24"
          fill="url(#mascot-tones)" role="img"
          aria-label="Cartoon cowboy mascot in hat, plaid shirt, denim overalls, gloves and boots, hands on hips"/>
    <text class="brand-name" x="992" y="215" font-size="62" text-anchor="middle">PORCHLIGHT PALS</text>
    <text class="contact-phone" x="390" y="302" font-size="40" text-anchor="middle">800-555-0143</text>
    <text class="contact-web" x="390" y="330" font-size="22" text-anchor="middle">porchlightpals.com</text>
  </g>
</svg>
</body>
</html>
```